Update Business Card Design

I'm looking to update my business cards. Attached is a photo of the current design. I like the black side so that does not have to be update. The white side needs to be updated. I want the design to be modern and minimalistic.
I am a lawyer and my firm's website is www.brennoxlegalco.com (for reference).
My firm's logo has a horizontal version (which is on the black side of the card) and a vertical version (on the white side). I would prefer to keep the vertical version on the white side and horizontal version on the black side (the logo files are attached).

I am open to redesigning the black side also. I would like one side to have the horizontal logo and the other to have the vertical logo.

```html
<!DOCTYPE html>
<html lang="en">
<head>
<meta charset="utf-8">
<title>Brennox Legal Co — Business Card</title>
<link rel="stylesheet" href="https://fonts.googleapis.com/css2?family=Cinzel:wght@500;700&family=Poppins:wght@400;500&display=swap">
<style>
  :root {
    --backdrop: #6f6f6f;
    --card-dark: #222222;
    --card-light: #ffffff;
    --brand-blue: #00b4e0;
    --rule-gray: #5a5a5a;
    --text-light: #ffffff;
  }
  * { margin: 0; padding: 0; box-sizing: border-box; }
  html, body {
    width: 1200px; height: 1015px; overflow: hidden;
    background: var(--backdrop);
  }
  .canvas { position: relative; width: 1200px; height: 1015px; }
  .card {
    position: absolute; left: 310px; width: 580px; height: 330px;
    overflow: hidden;
    box-shadow: 0 8px 18px rgba(0,0,0,0.35);
  }
  .card--back { top: 105px; background: var(--card-dark); }
  .card--front { top: 520px; background: var(--card-light); }

  /* Horizontal brand lockup */
  .lockup-horizontal {
    position: absolute; inset: 0;
    display: flex; align-items: center; justify-content: center; gap: 22px;
  }
  .brand-dot {
    width: 78px; height: 78px; border-radius: 50%;
    background: var(--brand-blue);
  }
  .lockup-divider { width: 1px; height: 96px; background: var(--rule-gray); }
  .brand-name {
    font-family: "Cinzel", serif; font-weight: 500;
    color: var(--brand-blue); line-height: 1.05;
  }
  .lockup-horizontal .brand-name { font-size: 34px; }

  /* Front side */
  .front-art { position: absolute; inset: 0; }
  .lockup-vertical {
    position: absolute; top: 32px; right: 36px; width: 200px;
    display: flex; flex-direction: column; align-items: center;
  }
  .lockup-vertical .brand-dot { width: 86px; height: 86px; }
  .lockup-vertical .lockup-rule {
    width: 180px; height: 2px; background: var(--rule-gray); margin: 14px 0 10px;
  }
  .lockup-vertical .brand-name { font-size: 26px; text-align: center; }

  .contact {
    position: absolute; left: 38px; bottom: 30px;
    color: var(--text-light);
    font-family: "Poppins", sans-serif; font-size: 13.5px; line-height: 1.42;
  }
  .contact-name {
    font-family: "Cinzel", serif; font-weight: 700; font-size: 21px; line-height: 1.1;
  }
  .contact-title { font-size: 14px; margin-bottom: 10px; }
  .contact-list { list-style: none; }
  .contact-list li { display: flex; align-items: center; gap: 10px; }
  .contact-list svg { width: 13px; height: 13px; flex: none; }
  .contact-address { margin-top: 10px; }
</style>
</head>
<body>
<main class="canvas">

  <section class="card card--back" aria-label="Card back">
    <div class="lockup-horizontal">
      <span class="brand-dot"></span>
      <span class="lockup-divider"></span>
      <span class="brand-name">Brennox<br>Legal Co</span>
    </div>
  </section>

  <section class="card card--front" aria-label="Card front">
    <svg class="front-art" viewBox="0 0 580 330" preserveAspectRatio="none" aria-hidden="true">
      <polygon points="0,0 196,0 393,330 0,330" fill="var(--brand-blue)"/>
      <line x1="182" y1="0" x2="379" y2="330" stroke="var(--card-light)" stroke-width="3.5"/>
    </svg>

    <div class="lockup-vertical">
      <span class="brand-dot"></span>
      <span class="lockup-rule"></span>
      <span class="brand-name">Brennox<br>Legal Co</span>
    </div>

    <div class="contact">
      <p class="contact-name">DANIEL OKAFOR</p>
      <p class="contact-title">Attorney at Law</p>
      <ul class="contact-list">
        <li>
          <svg viewBox="0 0 14 14"><rect x="3.5" y="1" width="7" height="12" rx="1.2" fill="none" stroke="#fff" stroke-width="1.3"/></svg>
          310.555.0142
        </li>
        <li>
          <svg viewBox="0 0 14 14"><path d="M3 1.5l2.5 0 1 3-1.5 1.2a7 7 0 0 0 3.3 3.3l1.2-1.5 3 1v2.5a1.5 1.5 0 0 1-1.6 1.5A11 11 0 0 1 1.5 3.1 1.5 1.5 0 0 1 3 1.5z" fill="#fff"/></svg>
          310.555.0187
        </li>
        <li>
          <svg viewBox="0 0 14 14"><rect x="3.5" y="1" width="7" height="4" fill="#fff"/><rect x="1" y="5" width="12" height="5" rx="1" fill="#fff"/><rect x="3.5" y="9" width="7" height="4" fill="#fff" stroke="#00b4e0" stroke-width="0.8"/></svg>
          310.555.0163
        </li>
        <li>
          <svg viewBox="0 0 14 14"><rect x="1" y="3" width="12" height="8.5" fill="#fff"/><path d="M1 3l6 5 6-5" fill="none" stroke="#00b4e0" stroke-width="1.1"/></svg>
          daniel@BrennoxLegalCo.com
        </li>
      </ul>
      <p class="contact-address">218 N. Alder Drive,<br>Suite 304 Fairview Hills,<br>CA 90000</p>
    </div>
  </section>

</main>
</body>
</html>
```